Software Engineering Company need eye catching banner for and Engineering conventions

We need an eye-catching banner designed. The size of the banner will be 34" W x 81" H. We develop routing software installed in bus systems and use GPS real-time tracking to always know where they are. We would like the banner to be dominated by the colors in our logo, 2 different blues, dark gray and of course white and black if needed. We are hoping for something that will pop out and look awesome. If you want to use our entire name or just our logo is completely up to you.

Target Market(s)

Young Engineers looking for new and cutting edge job opportunities

Industry/Entity Type

Computer Software

Colors
1f68ae
3779b6
ffffff

Requirements
Should not have
• the colors in our logo

```html
<!DOCTYPE html>
<html lang="en">
<head>
<meta charset="utf-8">
<title>Velora Technologies – Roll Up Banner</title>
<link rel="stylesheet" href="https://fonts.googleapis.com/css2?family=Montserrat:wght@300;400;600;800;900&display=swap">
<style>
  :root{
    --blue-deep:#1f68ae;
    --blue-mid:#3779b6;
    --blue-bright:#0b8fd3;
    --blue-sky:#5ec3ea;
    --blue-pale:#d3e4f2;
    --grey-dark:#4a4a4a;
    --grey-mid:#8a8a8a;
    --grey-text:#7a7a7a;
    --white:#ffffff;
    --mint:#7fd6c4;
  }
  *{margin:0;padding:0;box-sizing:border-box}
  html,body{width:1171px;height:1200px;overflow:hidden;background:var(--white)}
  body{font-family:'Montserrat',sans-serif;position:relative}
  .stage{position:absolute;left:0;top:0;width:1171px;height:1171px;
    background:linear-gradient(180deg,var(--blue-pale) 0%,#b7dbf1 35%,#3db5e3 75%,#0f9ad4 100%)}
  .presentation-title{position:absolute;left:123px;top:140px;color:var(--white)}
  .presentation-title .brand{font-weight:800;font-size:28px;letter-spacing:.5px;display:flex;align-items:center;gap:10px}
  .presentation-title .brand::before{content:"";width:26px;height:26px;background:var(--white)}
  .presentation-title .brand-sub{font-weight:400;font-size:7px;letter-spacing:3.5px;margin:2px 0 0 36px}
  .presentation-title h1{font-weight:900;font-size:26px;line-height:33px;margin-top:14px}

  .banner{position:absolute;left:377px;top:55px;width:448px;height:1062px;background:var(--white);overflow:hidden}
  .banner svg.art{position:absolute;left:0;top:0}
  .banner-head{position:absolute;right:40px;top:24px;color:var(--white)}
  .banner-head .web{font-size:8px;font-weight:600;display:flex;align-items:center;gap:3px}
  .banner-head .name{font-size:20px;font-weight:800;margin-top:6px;display:flex;align-items:center;gap:6px}
  .banner-head .name::before{content:"";width:18px;height:18px;border-radius:50%;background:var(--white)}
  .banner-head .sub{font-size:5px;letter-spacing:2px;margin-left:24px}

  .headline{position:absolute;left:33px;top:650px;color:var(--blue-mid);font-size:21px;line-height:32.5px;font-weight:300;white-space:nowrap}
  .headline strong{font-weight:800}

  .feature{position:absolute;top:762px;width:90px;margin-left:-45px;text-align:center}
  .feature--track{left:70px}
  .feature--training{left:175px}
  .feature--quality{left:273px}
  .feature-icon{width:49px;height:49px;border-radius:50%;margin:0 auto;
    background:linear-gradient(135deg,var(--blue-sky),var(--blue-deep));display:flex;align-items:center;justify-content:center}
  .feature h3{font-size:8.5px;font-weight:800;color:var(--grey-dark);line-height:11px;margin-top:10px}
  .feature p{font-size:6px;color:var(--grey-text);line-height:8.5px;margin-top:6px}

  .usage{position:absolute;left:33px;top:894px}
  .usage h4{font-size:10px;font-weight:800;color:var(--blue-mid)}
  .usage-row{display:flex;align-items:center;margin-top:9px;height:9px}
  .usage-row:first-of-type{margin-top:17px}
  .usage-row span{font-size:8px;color:var(--grey-dark);width:48px}
  .usage-bar{width:109px;height:8px;border-radius:4px;background:var(--grey-mid);overflow:hidden}
  .usage-bar i{display:block;height:100%;border-radius:4px;background:linear-gradient(90deg,#d8ecf8,var(--blue-bright))}

  .contact{position:absolute;left:33px;top:986px;font-size:7px;color:var(--grey-dark)}
  .contact li{list-style:none;display:flex;align-items:center;gap:15px;height:18px}
  .contact svg{width:10px;height:10px}
</style>
</head>
<body>
<div class="stage">
  <div class="presentation-title">
    <div class="brand">VELORA</div>
    <div class="brand-sub">TECHNOLOGIES LLC</div>
    <h1>Eye Catching<br>Roll Up Banner</h1>
  </div>

  <section class="banner">
    <svg class="art" width="448" height="1062" viewBox="0 0 448 1062">
      <defs>
        <linearGradient id="swoosh" x1="0" x2="1" y1="0" y2="0">
          <stop offset="0" stop-color="#0b86cc"/><stop offset=".6" stop-color="#6ccaf0"/><stop offset="1" stop-color="#0b8fd3"/>
        </linearGradient>
        <linearGradient id="cap" x1="0" y1="0" x2="1" y2="1">
          <stop offset="0" stop-color="#3fb6e8"/><stop offset="1" stop-color="#0a86cf"/>
        </linearGradient>
        <linearGradient id="routeArea" x1="0" y1="0" x2="0" y2="1">
          <stop offset="0" stop-color="#5ec3ea" stop-opacity=".25"/><stop offset="1" stop-color="#0b8fd3" stop-opacity=".55"/>
        </linearGradient>
        <linearGradient id="photoTone" x1="0" y1="0" x2="1" y2="1">
          <stop offset="0" stop-color="#e9eef5"/><stop offset=".6" stop-color="#b7c3d6"/><stop offset="1" stop-color="#243a66"/>
        </linearGradient>
        <linearGradient id="portraitTone" x1="0" y1="0" x2="1" y2="1">
          <stop offset="0" stop-color="#4a5160"/><stop offset=".5" stop-color="#d7b48e"/><stop offset="1" stop-color="#a9b8ea"/>
        </linearGradient>
        <linearGradient id="wave" x1="0" x2="1">
          <stop offset="0" stop-color="#2a8ad6"/><stop offset="1" stop-color="#0b8fd3"/>
        </linearGradient>
      </defs>

      <!-- top swoosh band -->
      <path d="M0 0 H448 L448 20 C380 40 320 60 230 45 C140 30 60 40 0 55 Z" fill="url(#swoosh)"/>
      <path d="M0 55 C60 40 140 30 230 45 C150 60 60 90 0 95 Z" fill="#8fd3f2" opacity=".45"/>
      <!-- header cap -->
      <path d="M200 0 H448 C430 70 400 110 360 114 C320 118 290 90 260 60 C240 40 220 20 200 0 Z" fill="url(#cap)"/>

      <!-- route artwork area -->
      <path d="M250 520 C300 580 448 600 448 640 V1000 C380 1000 320 1010 280 1040 C330 900 420 820 360 700 C320 640 230 600 250 520 Z"
            fill="url(#routeArea)" role="img" aria-label="Illustration: winding route with stop markers"/>

      <!-- big photo circle -->
      <circle cx="215" cy="308" r="213" fill="#1f8fd6"/>
      <circle cx="213" cy="308" r="207" fill="url(#photoTone)" role="img" aria-label="Photo: young engineer sketching app wireframes on a whiteboard"/>
      <!-- small portrait circle -->
      <circle cx="102" cy="496" r="91" fill="#1f8fd6"/>
      <circle cx="102" cy="496" r="86" fill="url(#portraitTone)" role="img" aria-label="Photo: smiling colleague in an office"/>

      <!-- bottom wave -->
      <path d="M0 1062 V1048 C80 1040 160 1040 220 1018 C260 1000 280 978 320 975 C360 978 400 992 448 980 V1062 Z" fill="#e9eef3"/>
      <path d="M25 1062 C100 1058 180 1050 230 1030 C262 1012 282 988 320 983 C360 986 400 996 448 986 V1062 Z" fill="url(#wave)"/>
      <path d="M25 1061 C100 1057 180 1049 230 1029 C262 1011 282 986 320 981" fill="none" stroke="#8fe0c8" stroke-width="4"/>
    </svg>

    <header class="banner-head">
      <div class="web">
        <svg width="6" height="8" viewBox="0 0 6 8"><path d="M3 0C1.3 0 0 1.3 0 3c0 2 3 5 3 5s3-3 3-5C6 1.3 4.7 0 3 0z" fill="none" stroke="#fff" stroke-width="1"/></svg>
        www.veloratech.example
      </div>
      <div class="name">VELORA</div>
      <div class="sub">TECHNOLOGIES LLC</div>
    </header>

    <h2 class="headline">We Develop<br><strong>The Best Route Planning</strong><br><strong>Software</strong> for Your Business</h2>

    <div class="feature feature--track">
      <div class="feature-icon"><svg width="28" height="28" viewBox="0 0 28 28" fill="none" stroke="#fff" stroke-width="1.3"><rect x="4" y="8" width="8" height="14" rx="1.5"/><circle cx="17" cy="13" r="7"/><path d="M10 13h14M17 6v14"/><path d="M22 3c-2 0-3 1-3 3 0 2 3 5 3 5s3-3 3-5c0-2-1-3-3-3z"/></svg></div>
      <h3>Track<br>Products</h3>
      <p>Easily track your products, employees, auto mobiles with our intuitive tracking software.</p>
    </div>
    <div class="feature feature--training">
      <div class="feature-icon"><svg width="28" height="28" viewBox="0 0 28 28" fill="none" stroke="#fff" stroke-width="1.3"><rect x="4" y="6" width="18" height="15" rx="1.5"/><path d="M4 10h18M8 15l5-2 5 2-5 2z"/><rect x="21" y="15" width="4" height="7" rx="2"/></svg></div>
      <h3>No Training<br>Required</h3>
      <p>Forget about multi-week training sessions or lengthy and tricky user manuals!</p>
    </div>
    <div class="feature feature--quality">
      <div class="feature-icon"><svg width="28" height="28" viewBox="0 0 28 28" fill="none" stroke="#fff" stroke-width="1.3"><circle cx="14" cy="11" r="7"/><path d="M14 7.5l1.1 2.3 2.4.3-1.8 1.7.5 2.4-2.2-1.2-2.2 1.2.5-2.4-1.8-1.7 2.4-.3z"/><path d="M9 16l-3 7 3-1 2 2 2-5M19 16l3 7-3-1-2 2-2-5"/></svg></div>
      <h3>Quality<br>Guaranteed</h3>
      <p>Get the quality of your money with our route planning software</p>
    </div>

    <div class="usage">
      <h4>Software Usage</h4>
      <div class="usage-row"><span>2011-2013</span><div class="usage-bar"><i style="width:46%"></i></div></div>
      <div class="usage-row"><span>2014-2016</span><div class="usage-bar"><i style="width:64%"></i></div></div>
      <div class="usage-row"><span>2017-2019</span><div class="usage-bar"><i style="width:86%"></i></div></div>
    </div>

    <ul class="contact">
      <li><svg viewBox="0 0 10 10"><path d="M2 0.5l2 2-1 1.3c.6 1.3 1.7 2.4 3 3L7.3 5.8l2 2L8.5 9.5C4 9.5 .5 6 .5 1.5z" fill="#4a4a4a"/></svg>+0123 555 0190 00</li>
      <li><svg viewBox="0 0 10 10"><rect x=".5" y="2" width="9" height="6.5" fill="#4a4a4a"/><path d="M.5 2l4.5 3.5L9.5 2" fill="none" stroke="#fff" stroke-width=".8"/></svg>hello@veloratech.example</li>
    </ul>
  </section>
</div>
</body>
</html>
```